Tidal Fern Business Cards

We need something new, fun and exciting for business cards. Our current ones are just plain and we need a design that pops. We want name, position held, phone, email on the front, and a 20% discount on the back. I have also uploaded our old business cards creative to see what we are not wanting, and how boring they were and we want something jazzed up from this, cool design and catches people attention.

```html
<!DOCTYPE html>
<html lang="en">
<head>
<meta charset="utf-8">
<title>Tidal Fern Business Cards</title>
<link href="https://fonts.googleapis.com/css2?family=Montserrat:wght@700;800;900&family=Arimo:wght@400&display=swap" rel="stylesheet">
<style>
  :root {
    --navy: #1b3d6d;
    --coral: #f07470;
    --orange: #ff4f0f;
    --paper: #ffffff;
    --ink-soft: #3a3a3a;
    --rule: #b9b9b9;
    --wash: #ececec;
    --stage: #2e2e2e;
  }
  * { box-sizing: border-box; margin: 0; padding: 0; }
  html, body { width: 1200px; height: 866px; overflow: hidden; }
  body {
    background: var(--stage);
    display: flex;
    flex-direction: column;
    align-items: center;
    justify-content: center;
    gap: 40px;
  }
  .card {
    position: relative;
    width: 680px;
    height: 389px;
    overflow: hidden;
    box-shadow: 0 10px 24px rgba(0,0,0,.45);
  }

  /* Front */
  .card--front { background: var(--paper); }
  .front__wash {
    position: absolute;
    left: 20px;
    top: -30px;
    width: 360px;
    height: 400px;
    background: radial-gradient(ellipse at center, var(--wash) 0%, rgba(236,236,236,.6) 45%, rgba(255,255,255,0) 72%);
  }
  .contact {
    position: absolute;
    left: 48px;
    top: 96px;
    color: var(--ink-soft);
    font-family: Arimo, Arial, sans-serif;
  }
  .contact__name {
    font-family: Montserrat, sans-serif;
    font-weight: 800;
    font-size: 26px;
    color: var(--navy);
    letter-spacing: .3px;
    line-height: 1.1;
  }
  .contact__role { font-size: 16px; margin: 2px 0 10px; }
  .contact__list { list-style: none; font-size: 16px; line-height: 23px; }
  .contact__list li { display: flex; align-items: center; gap: 8px; }
  .contact__list svg { width: 14px; height: 14px; flex: none; }
  .brand {
    position: absolute;
    right: 48px;
    top: 108px;
    display: flex;
    align-items: center;
    gap: 12px;
  }
  .brand__dot { width: 16px; height: 16px; border-radius: 50%; background: var(--coral); }
  .brand__name {
    font-family: Montserrat, sans-serif;
    font-weight: 800;
    font-size: 50px;
    color: var(--navy);
    letter-spacing: .5px;
    line-height: 1;
  }
  .divider {
    position: absolute;
    left: 300px;
    right: 48px;
    top: 246px;
    height: 1px;
    background: var(--rule);
  }
  .address {
    position: absolute;
    right: 48px;
    top: 268px;
    text-align: right;
    font-style: normal;
    font-family: Arimo, Arial, sans-serif;
    font-size: 18px;
    line-height: 25px;
    color: var(--ink-soft);
    letter-spacing: .8px;
  }

  /* Back */
  .card--back {
    background:
      radial-gradient(ellipse 42% 48% at 62% 78%, var(--navy) 0%, var(--navy) 55%, rgba(27,61,109,0) 100%),
      radial-gradient(ellipse 85% 95% at 55% 70%, var(--coral) 0%, var(--coral) 60%, #b85f6b 78%, var(--navy) 100%);
  }
  .back__art { position: absolute; inset: 0; }
  .offer {
    position: absolute;
    right: 92px;
    bottom: 68px;
    color: var(--orange);
    font-family: Montserrat, sans-serif;
    font-weight: 900;
    line-height: .85;
    text-align: center;
  }
  .offer__value { display: block; font-size: 110px; letter-spacing: -4px; }
  .offer__value sup { font-size: 30px; vertical-align: top; margin-left: 4px; letter-spacing: 0; }
  .offer__label { display: block; font-size: 46px; letter-spacing: 2px; margin-top: -6px; }
</style>
</head>
<body>

<section class="card card--front" aria-label="Business card front">
  <div class="front__wash" role="img" aria-label="Faint background brand motif area"></div>

  <div class="contact">
    <h1 class="contact__name">Marcus Hale</h1>
    <p class="contact__role">Managing Director</p>
    <ul class="contact__list">
      <li>
        <svg viewBox="0 0 14 14" aria-hidden="true"><rect x=".75" y=".75" width="12.5" height="12.5" fill="none" stroke="#1b3d6d" stroke-width="1.5"/><path d="M4.5 3.5c-1 1 0 4 2 6s4 2.5 4.5 1.5l-1.5-1.5-1 .8c-.8-.3-2.3-1.8-2.6-2.6l.8-1L5 3.3z" fill="#1b3d6d"/></svg>
        044-987 654 321
      </li>
      <li>
        <svg viewBox="0 0 14 14" aria-hidden="true"><rect x=".5" y="2.5" width="13" height="9" fill="#1b3d6d"/><path d="M.5 2.5 7 8l6.5-5.5" fill="none" stroke="#fff" stroke-width="1.2"/></svg>
        hello@tidalfern.com
      </li>
      <li>
        <svg viewBox="0 0 14 14" aria-hidden="true"><circle cx="7" cy="7" r="6.3" fill="none" stroke="#1b3d6d" stroke-width="1.4"/><ellipse cx="7" cy="7" rx="2.6" ry="6.3" fill="none" stroke="#1b3d6d" stroke-width="1.2"/><path d="M.7 7h12.6M1.8 4h10.4M1.8 10h10.4" stroke="#1b3d6d" stroke-width="1.1"/></svg>
        www.tidalfern.com
      </li>
    </ul>
  </div>

  <div class="brand">
    <span class="brand__dot" aria-hidden="true"></span>
    <span class="brand__name">Tidal Fern</span>
  </div>

  <div class="divider" aria-hidden="true"></div>

  <address class="address">
    88, Harbour Row Lane<br>
    Seaview City, 20418
  </address>
</section>

<section class="card card--back" aria-label="Business card back">
  <div class="back__art" role="img" aria-label="Large bold brand illustration of a heart with leaves in coral on navy"></div>
  <div class="offer">
    <span class="offer__value">20<sup>%</sup></span>
    <span class="offer__label">OFF</span>
  </div>
</section>

</body>
</html>
```